Highly rated moving company needs postcard design

We need a highly converting postcard to send when people put their homes for sale online. This should highlight the fact that we're Austin's highest rated moving company, and should convey quality and value. We do local, statewide and long distance moves. We also do office and commerical moves and storage. final design must be sized to work with our mailing system. Please see attached file for more information.

```html
<!DOCTYPE html>
<html lang="en">
<head>
<meta charset="utf-8">
<title>Summit Haulers Postcard</title>
<link href="https://fonts.googleapis.com/css2?family=Montserrat:wght@400;500;600;700;800&family=Exo+2:wght@600;700&family=Yellowtail&display=swap" rel="stylesheet">
<style>
:root{
  --navy:#0d0f91;
  --red:#ff1010;
  --white:#ffffff;
  --sky:#4f7dff;
  --line:#c8202a;
  --paper:#ffffff;
}
*{box-sizing:border-box;margin:0;padding:0}
html,body{width:848px;height:1200px;overflow:hidden;background:var(--paper)}
.canvas{position:relative;width:848px;height:1200px;font-family:"Montserrat",sans-serif}
.crop{position:absolute;background:#222}

/* front panel */
.front{position:absolute;left:68px;top:82px;width:712px;height:481px;background:var(--navy);color:var(--white);overflow:hidden}
.brand{position:absolute;left:90px;width:310px;top:42px;text-align:center;font-weight:600;color:var(--red);font-size:16px;letter-spacing:3px;white-space:nowrap}
.headline{font-weight:800;line-height:1;white-space:nowrap}
.headline span{position:absolute}
.headline .small{left:57px;top:102px;font-size:17px}
.headline .big{left:152px;top:92px;font-size:29px;color:var(--red);letter-spacing:-.5px}
.headline .line2{left:134px;top:132px;font-size:21px}
.rating{position:absolute;left:57px;top:184px;width:374px;height:16px}
.rating .rule{position:absolute;top:8px;height:1px;width:121px;background:var(--line)}
.rating .stars{position:absolute;left:132px;top:0;display:flex;gap:7px}
.script{font-family:"Yellowtail",cursive;color:var(--sky);font-size:20px;white-space:nowrap}
.about-title{position:absolute;left:57px;top:204px}
.about-text{position:absolute;left:54px;top:240px;width:298px;font-size:11px;line-height:15.5px;text-align:justify;font-weight:500}
.about-text strong{font-weight:700}
.about-text .hl{color:var(--red);font-weight:600}
.services-title{position:absolute;left:454px;top:46px}
.services{position:absolute;left:454px;top:86px;list-style:none;font-family:"Exo 2",sans-serif;font-weight:600;font-size:14.5px;line-height:15px;letter-spacing:.5px;white-space:nowrap}
.services li{position:relative;padding-left:30px;margin-bottom:15px}
.services li svg{position:absolute;left:0;top:1px}
.photo{position:absolute;left:386px;top:234px;width:278px;height:144px;background:linear-gradient(135deg,#d9c9b4,#a8835c 55%,#e9e2da)}
.contact{position:absolute;left:50px;top:392px}
.contact .ttl{font-size:21px;font-weight:600;line-height:1}
.contact .tag{display:inline-block;margin-top:4px;background:var(--red);color:var(--navy);font-weight:800;font-size:12px;padding:1px 3px}
.phone{position:absolute;left:200px;top:398px;font-family:"Exo 2",sans-serif;font-weight:700;font-size:31px;color:var(--red);letter-spacing:-.5px;white-space:nowrap}
.web{position:absolute;left:400px;top:408px;font-weight:700;font-size:16.5px;white-space:nowrap}

/* back */
.reviews-title{position:absolute;left:109px;top:662px;color:var(--red);font-size:20px}
.review{position:absolute;top:698px;width:205px;height:121px;background:var(--navy);color:var(--white);padding:13px 16px}
.review h3{font-size:12px;font-weight:700}
.review .stars{display:flex;gap:3px;margin-top:9px}
.review p{margin-top:10px;font-size:8.6px;line-height:12px;text-align:justify}
.divider{position:absolute;left:103px;width:645px;height:1.5px;background:var(--navy)}
.badge{position:absolute;top:848px;height:42px;border-radius:4px}
.product-photo{position:absolute;left:103px;top:915px;width:110px;height:171px;background:linear-gradient(160deg,#f2eee8,#c9a77a 60%,#e8e2d8)}
.back-mark{position:absolute;left:318px;top:924px;width:30px;height:30px;border-radius:50%;background:var(--navy)}
.back-brand{position:absolute;left:219px;top:964px;width:228px;text-align:center;color:var(--red);font-weight:600;font-size:15px;letter-spacing:2.5px;line-height:18px;white-space:nowrap}
.quote-bar{position:absolute;left:229px;top:996px;width:208px;height:20px;background:var(--navy);color:var(--white);font-weight:700;font-size:13.5px;text-align:center;line-height:20px;white-space:nowrap}
.back-phone{position:absolute;left:219px;top:1014px;width:228px;text-align:center;font-family:"Exo 2",sans-serif;font-weight:700;font-size:34px;line-height:40px;color:var(--red);letter-spacing:-.5px;white-space:nowrap}
.back-web{position:absolute;left:219px;top:1050px;width:228px;text-align:center;font-weight:700;font-size:13px;color:var(--navy);white-space:nowrap}
.back-address{position:absolute;left:209px;top:1068px;width:248px;text-align:center;font-weight:500;font-size:10.5px;letter-spacing:-.2px;color:var(--navy);white-space:nowrap}
.mailing{position:absolute;left:453px;top:917px;width:309px;height:183px;background:var(--red);color:var(--white);display:flex;align-items:center;justify-content:center;text-align:center;font-weight:700;font-size:15px;line-height:20px;padding-bottom:30px}
</style>
</head>
<body>
<svg width="0" height="0" style="position:absolute">
  <defs>
    <symbol id="star-box" viewBox="0 0 20 20">
      <rect width="20" height="20" fill="#ff1010"/>
      <path d="M10 3.2l2 4.3 4.6.5-3.4 3.1 1 4.6L10 13.4l-4.2 2.3 1-4.6L3.4 8l4.6-.5z" fill="#fff"/>
    </symbol>
    <symbol id="tick-box" viewBox="0 0 20 20">
      <rect width="20" height="20" fill="#ff1010"/>
      <path d="M4.5 10.5l4 4 7.5-9" fill="none" stroke="#fff" stroke-width="3"/>
    </symbol>
  </defs>
</svg>

<main class="canvas">
  <div class="crop" style="left:68px;top:82px;width:1px;height:8px"></div>
  <div class="crop" style="left:68px;top:82px;width:8px;height:1px"></div>
  <div class="crop" style="left:779px;top:82px;width:1px;height:8px"></div>
  <div class="crop" style="left:772px;top:82px;width:8px;height:1px"></div>
  <div class="crop" style="left:58px;top:645px;width:17px;height:1px"></div>
  <div class="crop" style="left:78px;top:626px;width:1px;height:18px"></div>
  <div class="crop" style="left:772px;top:645px;width:17px;height:1px"></div>
  <div class="crop" style="left:771px;top:626px;width:1px;height:18px"></div>
  <div class="crop" style="left:58px;top:1108px;width:17px;height:1px"></div>
  <div class="crop" style="left:78px;top:1110px;width:1px;height:18px"></div>
  <div class="crop" style="left:772px;top:1108px;width:17px;height:1px"></div>
  <div class="crop" style="left:771px;top:1110px;width:1px;height:18px"></div>

  <section class="front">
    <div class="brand">SUMMIT HAULERS</div>
    <h1 class="headline"><span class="small">AUSTIN'S</span><span class="big">HIGHEST RATED</span><span class="line2">MOVING COMPANY</span></h1>
    <div class="rating">
      <span class="rule" style="left:0"></span>
      <div class="stars">
        <svg width="16" height="16"><use href="#star-box"/></svg>
        <svg width="16" height="16"><use href="#star-box"/></svg>
        <svg width="16" height="16"><use href="#star-box"/></svg>
        <svg width="16" height="16"><use href="#star-box"/></svg>
        <svg width="16" height="16"><use href="#star-box"/></svg>
      </div>
      <span class="rule" style="left:253px"></span>
    </div>

    <div class="about-title script">about us</div>
    <p class="about-text"><strong>Summit Haulers</strong> is the <span class="hl">NO. 1 CHOICE</span> for residential and commercial moving labor in the Austin area. We're a moving company founded on the core values of honesty, dependability, adaptability, and respect. Hire us, and you know you're getting the strongest and most reliable moving team in the city. We dare say that we do more than provide stress-free moves — <span class="hl">WE MAKE MOVING FUN!</span></p>

    <div class="services-title script">our services</div>
    <ul class="services">
      <li><svg width="18" height="18"><use href="#tick-box"/></svg>RESIDENTIAL AND<br>COMMERCIAL MOVING</li>
      <li><svg width="18" height="18"><use href="#tick-box"/></svg>LONG-DISTANCE MOVING</li>
      <li><svg width="18" height="18"><use href="#tick-box"/></svg>PACKAGING SERVICES</li>
      <li><svg width="18" height="18"><use href="#tick-box"/></svg>PIANO MOVING</li>
    </ul>

    <div class="photo" role="img" aria-label="Photo of a smiling family carrying moving boxes and a rolled rug into their new home"></div>

    <div class="contact">
      <div class="ttl">CONTACT US</div>
      <div class="tag">FOR A FREE QUOTE</div>
    </div>
    <div class="phone">512-555-0147</div>
    <div class="web">www.summithaulersatx.com</div>
  </section>

  <section class="back">
    <div class="reviews-title script">customer reviews</div>

    <article class="review" style="left:103px">
      <h3>Daniel K.</h3>
      <div class="stars">
        <svg width="13" height="13"><use href="#star-box"/></svg><svg width="13" height="13"><use href="#star-box"/></svg><svg width="13" height="13"><use href="#star-box"/></svg><svg width="13" height="13"><use href="#star-box"/></svg><svg width="13" height="13"><use href="#star-box"/></svg>
      </div>
      <p>Summit Haulers did a superb job of packing and moving our house from Austin to California. Ray and Leo were professional, courteous and efficient.</p>
    </article>
    <article class="review" style="left:321px">
      <h3>Rosa T.</h3>
      <div class="stars">
        <svg width="13" height="13"><use href="#star-box"/></svg><svg width="13" height="13"><use href="#star-box"/></svg><svg width="13" height="13"><use href="#star-box"/></svg><svg width="13" height="13"><use href="#star-box"/></svg><svg width="13" height="13"><use href="#star-box"/></svg>
      </div>
      <p>The best movers ever! I am so grateful to have found Jordan and his crew. Super great people and the fastest, cleanest, most efficient move to date.</p>
    </article>
    <article class="review" style="left:541px">
      <h3>Clara P.</h3>
      <div class="stars">
        <svg width="13" height="13"><use href="#star-box"/></svg><svg width="13" height="13"><use href="#star-box"/></svg><svg width="13" height="13"><use href="#star-box"/></svg><svg width="13" height="13"><use href="#star-box"/></svg><svg width="13" height="13"><use href="#star-box"/></svg>
      </div>
      <p>Nick and Paul are fantastic. They safely move possessions, are time conscious, have a good sense of humor and actually made moving FUN.</p>
    </article>

    <div class="divider" style="top:831px"></div>
    <div class="badge" style="left:105px;width:112px;background:#f1f1f1"></div>
    <div class="badge" style="left:259px;width:83px;height:26px;top:850px;background:var(--navy)"></div>
    <div class="badge" style="left:387px;width:100px;background:#9fe3f0"></div>
    <div class="badge" style="left:534px;width:85px;background:#e23a3a"></div>
    <div class="badge" style="left:665px;width:78px;background:#2b2b2b"></div>
    <div class="divider" style="top:902px"></div>

    <div class="product-photo" role="img" aria-label="Photo of stacked cardboard moving boxes with a vase of flowers"></div>

    <span class="back-mark"></span>
    <div class="back-brand">SUMMIT HAULERS</div>
    <div class="quote-bar">CONTACT FOR FREE QUOTE</div>
    <div class="back-phone">512-555-0147</div>
    <div class="back-web">www.summithaulersatx.com</div>
    <div class="back-address">4820 Cedar Bluff Dr, Austin, TX 78745</div>

    <div class="mailing">MAILING<br>AREA</div>
  </section>
</main>
</body>
</html>
```